Holistic Health Coach needs simple web site design for a new practice

I need a web (re)design for my entire site, Birchwell Sprout Lady. I have a beautiful new blue and green logo that I'd like the site fonts and color scheme to be built around. I'll attach my new logo so you'll know the colors/design feel I'm after.

I want easy navigation for my mostly text based site, widgets for my social media pages and a clean, fun, light feel for the site.

Target Market(s)

People looking to take charge of their own health, and who may need my coaching services to obtain optimal wellness.

Industry/Entity Type

Health

Coding

Coded - Design and coding required

Number of Pages Required

5+ page

Font styles to use
Script

Colors
33b8a4
33a6d7
ffffff

Requirements
Must have
• Must incorporate my logo design, as well as same/similar fonts and color scheme.
• I'd like it to stay as close to the current design as possible.
Nice to have
• Would love to incorporate a hover over menu (for example, when a user hovers over "About", they will see the submenu in a floating design.
Should not have
• No dark colors or masculine feel

```html
<!DOCTYPE html>
<html lang="en">
<head>
<meta charset="utf-8">
<title>Birchwell Sprout Lady – Lifestyles of the Tired and Frazzled</title>
<link rel="stylesheet" href="https://fonts.googleapis.com/css2?family=Open+Sans:wght@400;600;700&family=Roboto+Slab:wght@700&family=Dancing+Script:wght@400&display=swap">
<style>
:root{
  --teal:#33b8a4;
  --blue:#33a6d7;
  --green:#7cc02a;
  --white:#ffffff;
  --page:#f1f1f1;
  --line:#dcdcdc;
  --text:#555b5e;
  --title:#333a3d;
  --link:#d9342b;
  --muted:#a9adaf;
  --orange:#f08a1c;
  --icon:#6f6f6f;
}
*{box-sizing:border-box;margin:0;padding:0}
html,body{width:961px;height:1200px;overflow:hidden}
body{background:var(--page);font-family:"Open Sans",Arial,sans-serif;color:var(--text);position:relative}
.site-header{position:absolute;left:0;top:0;width:961px;height:64px;background:var(--white);border-bottom:2px solid #d4d4d4}
.brand{position:absolute;left:111px;top:22px;font-size:20px;font-weight:600;color:var(--teal);letter-spacing:.2px}
.brand .dot{display:inline-block;width:8px;height:8px;border-radius:50%;background:var(--green);margin-left:5px;vertical-align:middle}
.main-nav{position:absolute;top:30px;font-size:11.5px;color:#2a7d9a}
.main-nav a{position:absolute;white-space:nowrap;text-decoration:none;color:#2a7d9a}
.main-nav a.current{color:var(--blue)}
.submenu{position:absolute;left:371px;top:64px;width:143px}
.submenu a{display:block;height:33px;line-height:33px;padding-left:22px;font-size:9.5px;color:var(--white);background:var(--blue);text-decoration:none;border-bottom:1px solid rgba(255,255,255,.5)}
.submenu a.hover{background:var(--green);width:143px}
.post{position:absolute;left:112px;top:73px;width:499px;height:1160px;background:var(--white);border:1px solid var(--line);border-radius:4px;padding:24px 36px 0 36px}
.post-title{font-family:"Roboto Slab",Georgia,serif;font-size:17.5px;line-height:21px;color:var(--title);font-weight:700;width:420px}
.post-meta{margin-top:17px;font-size:8.5px;color:#777;display:flex;gap:12px;align-items:center}
.post-meta svg{vertical-align:-1px;margin-right:4px}
.post p{font-size:9.6px;line-height:15.7px;margin-top:8px}
.post p.lead{margin-top:17px}
.post a{color:var(--link);text-decoration:none}
.figure{display:block;margin:0 auto}
.fig-apple{width:76px;height:85px;margin-top:23px;margin-bottom:16px;background:radial-gradient(circle at 50% 55%,#c8202f 0 55%,transparent 57%)}
.fig-photo{width:98px;height:99px;margin-top:34px;margin-bottom:30px;background:linear-gradient(160deg,#cfa98a,#6f5a4c 60%,#3d3a3a)}
.fig-badge{width:98px;height:98px;border-radius:50%;margin-top:12px;margin-bottom:8px;background:#e06b2b}
.widget{position:absolute;left:629px;width:218px;background:var(--white);border:1px solid var(--line);border-radius:4px}
.promo{top:73px;height:219px;padding:10px}
.promo-art{width:197px;height:197px;background:linear-gradient(180deg,#f2f2f2 0 30%,#e9eef2 30% 70%,#f5f5f5 70%);position:relative}
.promo-art .hd{position:absolute;left:0;right:0;top:8px;text-align:center;font-size:12.5px;line-height:15px;font-weight:600;color:#333;letter-spacing:.3px}
.promo-art .hd b{font-weight:700}
.promo-art .help{position:absolute;left:0;right:0;top:150px;text-align:center;font-size:14px;font-style:italic;color:#444}
.promo-art .cta{position:absolute;left:42px;top:166px;width:106px;height:24px;background:var(--orange);border-radius:3px;color:var(--white);font-size:10.5px;font-weight:700;text-align:center;line-height:24px}
.promo-art .books{position:absolute;left:10px;top:62px;width:110px;height:80px;background:linear-gradient(120deg,#8fb9cf,#d6593b 50%,#3a6e96)}
.promo-art .seal{position:absolute;left:124px;top:68px;width:66px;height:66px;border-radius:50%;background:var(--blue)}
.widget-title{font-family:"Dancing Script",cursive;font-size:19px;color:#7bb93c;text-align:center;margin-top:12px}
.rule{display:block;margin:10px auto 0}
.newsletter{top:303px;height:369px;padding:0 10px}
.newsletter .intro{font-size:8.7px;line-height:12px;color:var(--muted);margin-top:16px;width:200px}
.field-label{font-size:9px;font-weight:600;color:#888;margin-top:12px}
.field{height:20px;border:1px solid var(--line);border-radius:2px;margin-top:5px;width:197px}
.req{font-size:9px;color:var(--muted);margin-top:12px}
.subscribe{display:block;margin:14px auto 0;width:159px;height:23px;background:var(--teal);color:var(--white);font-size:10px;text-align:center;line-height:23px;border-radius:3px}
.powered{text-align:center;font-size:9px;color:var(--muted);margin-top:16px}
.follow{top:687px;height:116px}
.social{display:flex;justify-content:center;gap:4px;margin-top:10px}
.social span{width:29px;height:29px;border-radius:50%;background:var(--icon)}
.social span.alt{background:var(--blue)}
.feed{top:818px;height:375px}
.grid{display:grid;grid-template-columns:repeat(4,41px);gap:6px 6px;justify-content:center;margin-top:18px;column-gap:6.5px}
.grid span{height:41px;display:block}
.feed-actions{display:flex;gap:4px;justify-content:center;margin-top:10px}
.btn{height:22px;line-height:22px;font-size:9.5px;color:var(--white);font-weight:600;border-radius:3px;padding:0 10px}
.btn.teal{background:var(--teal)}
.btn.green{background:var(--green)}
</style>
</head>
<body>
<header class="site-header">
  <div class="brand">Birchwell Sprout Lady<span class="dot"></span></div>
  <nav class="main-nav">
    <a class="current" style="left:386px">About Wren</a>
    <a style="left:479px">Articles</a>
    <a style="left:556px">Essential Oil</a>
    <a style="left:657px">21 -Day Sweet Reset Coaching Services</a>
  </nav>
</header>

<article class="post">
  <h1 class="post-title">Lifestyles of the Tired and Frazzled: Module 4 of Root Rehab: Adrenal Fatigue</h1>
  <div class="post-meta">
    <span><svg width="9" height="9" viewBox="0 0 9 9"><rect x=".5" y="1.5" width="8" height="7" fill="none" stroke="#33a6d7"/><rect x=".5" y="1.5" width="8" height="2" fill="#33a6d7"/></svg>April 5, 2015</span>
    <span><svg width="10" height="9" viewBox="0 0 10 9"><ellipse cx="5" cy="4" rx="4.3" ry="3.3" fill="none" stroke="#33a6d7"/></svg>Leave a comment</span>
  </div>
  <p class="lead">As the title suggests, Module 4 of Root Rehab: Adrenal Fatigue is all about lifestyle factors. Specifically, how you can make changes to your lifestyle in the areas of stress, sleep, social connection, and exercise and recovery.</p>
  <div class="figure fig-apple" role="img" aria-label="Red apple illustration with a medical cross"></div>
  <p>I've been dreading this module because when I got my IBS diagnosis, I was told that once I got my stress under control, my symptoms would go away. Which is partially true, but I had to make dietary changes, and undergo treatment for SIBO before I really started seeing improvement. And I wasn't sure there wasn't anything I could learn that I didn't already know in these areas.</p>
  <p>The first lesson in Module 4 covered stress management. There was a video discussing the effects of stress on the body, why stress management is so important, and several ideas that you can implement right away to help minimize the damage stress inflicts on the body. I think my favorite tools were the Stress Management Log and the variety of stress management tools they recommended – most of which were absolutely FREE. After just a few days of implementing the suggestions I selected, I am starting to see a difference in my mood and energy levels 🙂</p>
  <div class="figure fig-photo" role="img" aria-label="Photo of a frustrated woman biting a laptop"></div>
  <p>Next is sleep. No, I don't mean its time for a nap, but if you need one, by all means, take one and read this later. As in the previous lesson, I really thought I had this one nailed. Until I read the section about electronics and screen time. I 'knew' that you're not supposed to expose yourself to blue light after dark, or if you do, you should wear those funky looking orange glasses, because of its effect on your sleep, but I wasn't doing it. You see, blogging isn't my only job, and I have to work around my 9 to 5 job to find time to blog. Oftentimes, that means writing before the sun comes up or after it goes down. I do have <a>Dimlight</a> on my laptop, which helps A LOT, but then I'm often checking my phone, which until recently didn't have any sort of dimmer during the evening and early morning. I recently installed <a>Duskmode</a> on my smartphone as well. However, I was still checking my phone while in bed trying to get to sleep. If you're doing that, stop it. Really. I know it seems like an easy thing to do, but don't. It just really messes with your sleep, which is what you're trying to avoid, and doesn't help anyone. If you have to, buy a cheap alarm clock and use that so you can keep your phone in another room to charge at night. Okay…stepping off the soapbox now. Besides, we still have two more lessons to cover.</p>
  <p>Social Connection was the hardest lesson of the entire module for me. Not because the suggestions were hard to implements, they aren't. The hardest part was realizing that while I was sitting behind the screen of my laptop and working my 40-hr/week job, I wasn't developing relationships. With my family, with friends, with anyone – unless you count my laptop or social feeds as a relationship – which I don't . It was a sad revelation because I tend to be such a relationship oriented person. I'm starting to implement the suggestions from the lesson, and I was especially struck by a resource called <a>Harborline</a>. It's just what I needed to get my relationships back where I want them, and to strengthen newly formed relationships.</p>
  <div class="figure fig-badge" role="img" aria-label="Orange round badge for the Harborline resource"></div>
  <p>The final lesson covers exercise and recovery. I think this one will be a real eye opener for some – especially those in the Paleo/Real Food/Ancestral Health community. But I think it's SUCH an important message because too many people don't realize the proper role of exercise in Adrenal Fatigue/HPA Axis Dysregulation recovery. There are some great suggestions for how you can</p>
</article>

<nav class="submenu">
  <a>Sub menu 1</a>
  <a class="hover">Sub menu 1</a>
  <a>Sub menu 1</a>
  <a>Sub menu 1</a>
</nav>

<aside class="widget promo">
  <div class="promo-art">
    <div class="hd">NEED <b>EXTRA SUPPORT</b><br>TO <b><i>ROCK</i></b> YOUR<br><b>21-DAY SWEET RESET?</b></div>
    <div class="books" role="img" aria-label="Stack of program guidebooks"></div>
    <div class="seal" role="img" aria-label="Plain certification seal"></div>
    <div class="help">I'm here to help</div>
    <div class="cta">TELL ME MORE!</div>
  </div>
</aside>

<aside class="widget newsletter">
  <h2 class="widget-title">Sign Up for Newsletter</h2>
  <svg class="rule" width="198" height="8" viewBox="0 0 198 8"><line x1="0" y1="4" x2="198" y2="4" stroke="#c9c9c9"/></svg>
  <p class="intro">Exclusive, subscribers-only content delivered straight to your inbox</p>
  <div class="field-label">Email Address*</div><div class="field"></div>
  <div class="field-label" style="margin-top:16px">First Name</div><div class="field"></div>
  <div class="field-label" style="margin-top:16px">Last Name</div><div class="field"></div>
  <div class="req">* = required field</div>
  <div class="subscribe">Subscribe</div>
  <div class="powered">powered by PostPigeon!</div>
</aside>

<aside class="widget follow">
  <h2 class="widget-title">Follow Me</h2>
  <svg class="rule" width="198" height="8" viewBox="0 0 198 8"><line x1="0" y1="4" x2="198" y2="4" stroke="#c9c9c9"/></svg>
  <div class="social" aria-label="Social profiles"><span></span><span class="alt"></span><span></span><span></span></div>
</aside>

<aside class="widget feed">
  <h2 class="widget-title">Birchwell Sprout Lady on Photofeed</h2>
  <svg class="rule" width="198" height="8" viewBox="0 0 198 8"><line x1="0" y1="4" x2="198" y2="4" stroke="#c9c9c9"/></svg>
  <div class="grid" role="img" aria-label="Grid of recent feed photos">
    <span style="background:#8a7a5e"></span><span style="background:#b08a6a"></span><span style="background:#9d9a8e"></span><span style="background:#b52a3c"></span>
    <span style="background:#7c7f86"></span><span style="background:#4e4438"></span><span style="background:#3a3836"></span><span style="background:#9aa0a6"></span>
    <span style="background:#2f3f7a"></span><span style="background:#6c5c4a"></span><span style="background:#8c7060"></span><span style="background:#7b7464"></span>
    <span style="background:#3e3e52"></span><span style="background:#8a7f70"></span><span style="background:#6f8db4"></span><span style="background:#e2c21c"></span>
    <span style="background:#5a564c"></span><span style="background:#273a66"></span><span style="background:#4c4a4a"></span><span style="background:#5e6478"></span>
  </div>
  <div class="feed-actions"><span class="btn teal">Load More</span><span class="btn green">Follow Us on Photofeed</span></div>
</aside>
</body>
</html>
```